Oak Lumen Trail Home Page

Redesign the home page -- make it look more attractive and inviting.
Do we need to cut down on the wording? Probably -
Want a cleaner design.
Can go to www.OakLumenTrail.org for the website

```html
<!DOCTYPE html>
<html lang="en">
<head>
<meta charset="utf-8">
<title>Oak Lumen Trail – Home</title>
<link href="https://fonts.googleapis.com/css2?family=Montserrat:wght@400;500;600;700;800&family=Open+Sans:wght@400;600&display=swap" rel="stylesheet">
<style>
:root{
  --navy:#0a2a63;
  --blue:#1565d8;
  --blue-bright:#1e74ea;
  --deep:#0b1f44;
  --green:#16b55a;
  --green-dark:#0f9a4a;
  --orange:#f5a300;
  --red:#e5322d;
  --ink:#1d2433;
  --text:#5b6475;
  --muted:#9aa3b2;
  --line:#e4e8ef;
  --soft:#f3f5f9;
  --white:#ffffff;
}
*{box-sizing:border-box;margin:0;padding:0}
html,body{width:1200px;height:4808px;overflow:hidden}
body{font-family:"Open Sans",Arial,sans-serif;color:var(--text);background:var(--white);position:relative}
h1,h2,h3,h4,.btn,.brand,.nav a{font-family:"Montserrat",Arial,sans-serif}
.btn{display:inline-block;background:var(--green);color:var(--white);font-weight:600;font-size:15px;padding:13px 30px;border-radius:6px;text-decoration:none}

/* hero */
.hero{position:absolute;left:0;top:0;width:1200px;height:640px;background:linear-gradient(115deg,#0a3a86 0%,#0b4aa6 45%,#0e58c4 100%);overflow:hidden}
.hero-curve{position:absolute;left:0;top:0}
.topbar{position:absolute;left:40px;top:22px;width:1120px;height:40px;display:flex;align-items:center}
.brand{display:flex;align-items:center;gap:10px;color:var(--white);font-weight:700;font-size:18px}
.brand-dot{width:22px;height:22px;border-radius:50%;background:var(--green)}
.nav{position:absolute;left:430px;display:flex;gap:36px}
.nav a{color:var(--white);font-size:15px;font-weight:500;text-decoration:none}
.login{position:absolute;right:0;border:2px solid var(--white);color:var(--white);font-family:"Montserrat",sans-serif;font-weight:600;font-size:14px;padding:6px 22px;border-radius:6px}
.hero-copy{position:absolute;left:150px;top:205px;width:560px;color:var(--white)}
.hero-copy .kicker{font-family:"Montserrat",sans-serif;font-size:24px;font-weight:600}
.hero-copy h1{font-size:38px;line-height:1.22;font-weight:800;margin-top:16px}
.hero-copy .stat{font-family:"Montserrat",sans-serif;font-size:22px;font-weight:600;margin-top:20px}
.hero-copy .small{font-size:14px;line-height:1.45;margin-top:10px;opacity:.9}
.hero-copy .btn{margin-top:28px}
.hero-media{position:absolute;left:720px;top:208px;width:380px;height:264px;border-radius:14px;background:linear-gradient(135deg,#b8a37a,#7f6b4b 55%,#4d4030);box-shadow:0 18px 40px rgba(0,0,0,.35)}
.play{position:absolute;left:164px;top:106px}

/* pricing */
.pricing{position:absolute;left:0;top:640px;width:1200px;height:1000px;background:var(--white)}
.card{position:absolute;top:180px;width:430px;height:770px;background:var(--white);border-radius:14px;box-shadow:0 10px 40px rgba(20,40,80,.12);overflow:hidden}
.card-head{height:70px;display:flex;align-items:center;justify-content:center;font-family:"Montserrat",sans-serif;font-weight:700;font-size:22px;color:var(--white)}
.card.silver .card-head{background:#bfc4cc}
.card.gold{border:3px solid var(--orange)}
.card.gold .card-head{background:var(--orange)}
.card-body{padding:32px 34px}
.card h3{font-size:22px;font-weight:800;color:var(--ink)}
.card .sub{font-size:14px;color:var(--ink);margin-top:10px;line-height:1.5;min-height:62px;padding-bottom:18px;border-bottom:1px solid var(--line)}
.price-row{position:relative;height:56px;margin-top:26px}
.tag{position:absolute;left:0;top:0;width:250px;height:52px;color:var(--white);font-family:"Montserrat",sans-serif;font-weight:700;font-size:20px;display:flex;align-items:center;padding-left:34px;clip-path:polygon(0 0,92% 0,100% 50%,92% 100%,0 100%)}
.silver .tag{background:var(--green)}
.gold .tag{background:var(--red)}
.was{position:absolute;right:20px;top:14px;font-family:"Montserrat",sans-serif;font-size:20px;color:var(--muted);text-decoration:line-through}
.now{text-align:center;margin-top:24px;font-family:"Montserrat",sans-serif}
.now small{font-size:13px;color:var(--muted);margin-right:8px}
.now b{font-size:38px;font-weight:800;color:var(--ink)}
.gold .now b{color:var(--orange)}
.start{display:block;width:150px;margin:20px auto 0;text-align:center;font-family:"Montserrat",sans-serif;font-size:13px;font-weight:600;padding:9px 0;border-radius:6px;color:var(--white)}
.silver .start{background:#3d4452}
.gold .start{background:var(--orange)}
.features{list-style:none;margin-top:28px}
.features li{display:flex;gap:16px;align-items:flex-start;font-size:16px;color:var(--ink);padding:13px 0;border-top:1px solid var(--line);line-height:1.4}
.features li svg{flex:none;margin-top:1px}
.features li.off{color:#c3c8d0}
.gold .features li.hl{color:var(--blue)}

/* feature rows */
.row-media{position:absolute;border-radius:12px}
.row-copy{position:absolute;width:460px}
.row-copy h2{font-size:28px;line-height:1.3;font-weight:700;color:var(--ink)}
.row-copy .lead{font-family:"Montserrat",sans-serif;font-size:24px;line-height:1.35;color:#6a7385;margin-top:14px}
.row-copy p{font-size:16px;line-height:1.75;margin-top:18px}
.row-copy .btn{margin-top:26px}

/* testimonial */
.testimonial{position:absolute;left:0;top:3520px;width:1200px;height:520px;background:var(--soft)}
.quote-mark{position:absolute;left:150px;top:104px;font-family:Georgia,serif;font-size:150px;line-height:1;color:var(--blue);font-weight:700}
.quote{position:absolute;left:150px;top:280px;width:420px;font-size:17px;line-height:1.8;color:var(--ink)}
.testimonial .btn{position:absolute;left:150px;top:456px;background:var(--green)}
.person{position:absolute;left:680px;top:152px;width:370px;height:336px;background:linear-gradient(160deg,#8fa3b8,#5b6e80 55%,#3f4c59)}
.person-name{position:absolute;left:680px;top:496px;font-family:"Montserrat",sans-serif;font-weight:600;font-size:18px;color:var(--ink)}

/* cta */
.cta{position:absolute;left:0;top:4160px;width:1200px;height:340px;background:var(--blue-bright);text-align:center;color:var(--white)}
.cta h2{font-size:44px;font-weight:700;line-height:1.2;margin-top:48px}
.cta p{width:820px;margin:26px auto 0;font-size:15px;line-height:1.7;opacity:.95}
.cta .btn{margin-top:26px;background:var(--orange);font-size:14px;padding:11px 30px}

/* footer */
.footer{position:absolute;left:0;top:4500px;width:1200px;height:308px;background:var(--deep);color:#c7cfdd}
.footer .brand{position:absolute;left:72px;top:44px;font-size:18px}
.socials{position:absolute;left:72px;top:120px;display:flex;gap:16px}
.socials span{width:18px;height:18px;border:2px solid #8d9ab0;border-radius:3px}
.fcol{position:absolute;top:44px}
.fcol h4{font-size:14px;color:var(--blue-bright);font-weight:600;margin-bottom:14px}
.fcol a{display:block;color:#c7cfdd;font-size:14px;line-height:2.1;text-decoration:none}
.contact{position:absolute;left:990px;top:44px;font-size:14px;line-height:1.7}
.contact .phone{margin-top:22px}
</style>
</head>
<body>

<header class="hero">
  <svg class="hero-curve" width="1200" height="640" viewBox="0 0 1200 640" aria-hidden="true">
    <path d="M720 640 C820 470 1000 440 1200 380 L1200 640 Z" fill="#1a6ce6" opacity=".55"/>
    <path d="M0 590 C300 650 700 640 1200 560 L1200 640 L0 640 Z" fill="#ffffff"/>
  </svg>
  <div class="topbar">
    <div class="brand"><span class="brand-dot"></span>Oak Lumen Trail</div>
    <nav class="nav"><a href="#">Home</a><a href="#">Testimonials</a><a href="#">Was Scores</a><a href="#">FAQ</a><a href="#">Blog</a></nav>
    <span class="login">Login</span>
  </div>
  <div class="hero-copy">
    <div class="kicker">Recognized as</div>
    <h1>The BEST Credit Score<br>Improvement Program</h1>
    <div class="stat">81 Average Point Improvement</div>
    <div class="small">Request Your Lender's Credit Report<br>See What Your Lender Sees<br>Grow The Lender Credit Scores</div>
    <a class="btn" href="#">Get Started</a>
  </div>
  <div class="hero-media" role="img" aria-label="Video thumbnail showing a spread of paper currency">
    <svg class="play" width="52" height="52" viewBox="0 0 52 52" aria-hidden="true"><circle cx="26" cy="26" r="26" fill="#fff" opacity=".9"/><path d="M21 16 L37 26 L21 36 Z" fill="#1565d8"/></svg>
  </div>
</header>

<section class="pricing">
  <article class="card silver" style="left:152px">
    <div class="card-head">Good</div>
    <div class="card-body">
      <h3>SILVER</h3>
      <div class="sub">Lender's Report, Lender's Scores &amp; Analysis</div>
      <div class="price-row"><div class="tag">5% OFF</div><div class="was">$63.10</div></div>
      <div class="now"><small>only</small><b>$59.95</b></div>
      <span class="start">Get Started</span>
      <ul class="features">
        <li><svg width="22" height="22" viewBox="0 0 22 22"><circle cx="11" cy="11" r="11" fill="#16b55a"/><path d="M6 11.5l3.5 3.5L16 8" stroke="#fff" stroke-width="2.4" fill="none"/></svg>Lender-Grade Credit Scores Lenders use</li>
        <li><svg width="22" height="22" viewBox="0 0 22 22"><circle cx="11" cy="11" r="11" fill="#16b55a"/><path d="M6 11.5l3.5 3.5L16 8" stroke="#fff" stroke-width="2.4" fill="none"/></svg>Complete Credit Score Analysis</li>
        <li><svg width="22" height="22" viewBox="0 0 22 22"><circle cx="11" cy="11" r="11" fill="#16b55a"/><path d="M6 11.5l3.5 3.5L16 8" stroke="#fff" stroke-width="2.4" fill="none"/></svg>Potential Mortgage and Auto Loan Qualifications</li>
        <li class="off"><svg width="22" height="22" viewBox="0 0 22 22"><circle cx="11" cy="11" r="11" fill="#dfe3e9"/><path d="M6 11.5l3.5 3.5L16 8" stroke="#fff" stroke-width="2.4" fill="none"/></svg>Personalized Solutions to Higher Lender-Grade Credit Scores</li>
      </ul>
    </div>
  </article>
  <article class="card gold" style="left:620px">
    <div class="card-head">Best Offer</div>
    <div class="card-body">
      <h3>GOLD</h3>
      <div class="sub">Lender's Report, Lender's Scores, Analysis &amp; Steps to Score Improvement</div>
      <div class="price-row"><div class="tag">15% OFF</div><div class="was">$94.06</div></div>
      <div class="now"><small>only</small><b>$79.95</b></div>
      <span class="start">Get Started</span>
      <ul class="features">
        <li><svg width="22" height="22" viewBox="0 0 22 22"><circle cx="11" cy="11" r="11" fill="#16b55a"/><path d="M6 11.5l3.5 3.5L16 8" stroke="#fff" stroke-width="2.4" fill="none"/></svg>Lender-Grade Credit Scores Lenders use</li>
        <li><svg width="22" height="22" viewBox="0 0 22 22"><circle cx="11" cy="11" r="11" fill="#16b55a"/><path d="M6 11.5l3.5 3.5L16 8" stroke="#fff" stroke-width="2.4" fill="none"/></svg>Complete Credit Score Analysis</li>
        <li><svg width="22" height="22" viewBox="0 0 22 22"><circle cx="11" cy="11" r="11" fill="#16b55a"/><path d="M6 11.5l3.5 3.5L16 8" stroke="#fff" stroke-width="2.4" fill="none"/></svg>Potential Mortgage and Auto Loan Qualifications</li>
        <li class="hl"><svg width="22" height="22" viewBox="0 0 22 22"><circle cx="11" cy="11" r="11" fill="#16b55a"/><path d="M6 11.5l3.5 3.5L16 8" stroke="#fff" stroke-width="2.4" fill="none"/></svg>Personalized Solutions to Higher Lender-Grade Credit Scores</li>
      </ul>
    </div>
  </article>
</section>

<section>
  <div class="row-media" style="left:140px;top:1760px;width:370px;height:280px;background:linear-gradient(135deg,#e6f0fb,#cfe2f7 60%,#f4dccd)" role="img" aria-label="Illustration of a credit score gauge with a person at a desk"></div>
  <div class="row-copy" style="left:608px;top:1745px">
    <h2>See What Your Lenders See</h2>
    <div class="lead">Get the Same Credit Report and Scores Lenders Use</div>
    <p>As a Certified Credit Counselor, We Provide the Same Credit Report and 3 Scores Used by Mortgage &amp; Auto Lenders. Don't be Misled by "Unreliable Internet Credit Scores" - Not Knowing Accurate Scores could Cost You Lots of Money.</p>
    <a class="btn" href="#">Learn More</a>
  </div>

  <div class="row-copy" style="left:150px;top:2140px">
    <h2>Work with the BEST Credit Score Improvement Program</h2>
    <p>Oak Lumen Trail Averages an Amazing 81 Point Improvement for all 3 Lender-Grade Scores<br>Identifies Accounts to Pay Down by Priority, to Close, to Use, to Open, to Refinance, and to Consolidate</p>
    <a class="btn" href="#">Learn More</a>
  </div>
  <div class="row-media" style="left:720px;top:2140px;width:330px;height:360px;background:linear-gradient(150deg,#e9ecf8,#c9cdf0 50%,#f7c9c0)" role="img" aria-label="Illustration of people assembling puzzle pieces"></div>

  <div class="row-media" style="left:140px;top:2700px;width:370px;height:290px;background:linear-gradient(140deg,#eef3fb,#dbe6f7 55%,#f6e3b4)" role="img" aria-label="Illustration of a person leaping over stacks of coins"></div>
  <div class="row-copy" style="left:608px;top:2705px">
    <h2>Want to Know Your Potential Mortgage and Auto Loan Qualifications</h2>
    <p>Since We Provide the Same Credit Scores Lenders Use, We Give You Insight to Your Loan Qualifications<br>See What Mortgage and Auto Loan Options Work Best for You, Don't Wait for a Loan Officer</p>
    <a class="btn" href="#">Learn More</a>
  </div>

  <div class="row-copy" style="left:150px;top:3180px">
    <h2>Improve Your Purchasing Power by Increasing Your Lender's Credit Scores</h2>
    <p>Loan Officers Don't Care If You are Paying $130's More on Your Mortgage or Auto Loan Payment - You're Paying It! Most Home and Auto Buyers have Higher Payments because of Less-than-Excellent Credit Scores - Usually Less than 760</p>
    <a class="btn" href="#">Learn More</a>
  </div>
  <div class="row-media" style="left:680px;top:3180px;width:400px;height:260px;background:linear-gradient(160deg,#eef2fa,#d6e1f4 55%,#f3d9c7)" role="img" aria-label="Illustration of a team beside a rising bar chart"></div>
</section>

<section class="testimonial">
  <div class="quote-mark">&ldquo;</div>
  <p class="quote">I had my identity stolen right in the middle of the time that I put money down on a new home. I was able to clean my home and get the interest rate points to where I needed. We saved around $80/month.</p>
  <a class="btn" href="#">See Testimonials</a>
  <div class="person" role="img" aria-label="Portrait photo of a smiling client wearing a cap"></div>
  <div class="person-name">Marcus</div>
</section>

<section class="cta">
  <h2>Requesting Your Lender's Credit Report<br>Thru Oak Lumen Trail</h2>
  <p>Get the exact report and scores your lender will review before you apply. We walk you through every account, show which steps raise your scores fastest, and help you reach better rates on your next mortgage or auto loan with clear guidance.</p>
  <a class="btn" href="#">Get Started NOW</a>
</section>

<footer class="footer">
  <div class="brand"><span class="brand-dot"></span>Oak Lumen Trail</div>
  <div class="socials"><span></span><span></span></div>
  <div class="fcol" style="left:420px"><h4>Quick Menu</h4><a href="#">Home</a><a href="#">Testimonials</a><a href="#">Was Scores</a><a href="#">FAQ</a><a href="#">Blog</a></div>
  <div class="fcol" style="left:600px"><h4>Policy</h4><a href="#">Term Of Use</a><a href="#">Privacy Statement</a></div>
  <div class="contact">The Harbor Lane, Suite 210,<br>Millbrook, Oregon 97001<div class="phone">(555) 014-2290</div></div>
</footer>

</body>
</html>
```